Cardiology practice business card

We need a business card for our cardiology practice "Bellmoor Cardiology". We have a new logo, attached below. We like the colours in the logo - red and charcoal. The front of the business card will need to have the doctors name, address, phone number and email. The back will need to have space to write 2 appointment dates and times.

```html
<!DOCTYPE html>
<html lang="en">
<head>
<meta charset="utf-8">
<title>Bellmoor Cardiology — Business Card</title>
<link rel="stylesheet" href="https://fonts.googleapis.com/css2?family=Montserrat:wght@400;500;600;700&display=swap">
<style>
  :root{
    --red:#c8102e;
    --red-dark:#a50d25;
    --charcoal:#4a4a4c;
    --grey:#8a8a8c;
    --line:#cfcfd1;
    --paper:#ffffff;
    --board-top:#ffffff;
    --board-bottom:#e8e8ea;
  }
  *{margin:0;padding:0;box-sizing:border-box}
  html,body{width:1200px;height:2492px;overflow:hidden}
  body{font-family:"Montserrat",Arial,sans-serif;background:var(--board-bottom);position:relative}
  .sheet-top{position:absolute;left:0;top:0;width:1200px;height:1196px;background:var(--board-top);border-bottom:1px solid #dcdcde}
  .sheet-bottom{position:absolute;left:0;top:1196px;width:1200px;height:1296px;background:var(--board-bottom)}
  .card{position:absolute;filter:drop-shadow(0 3px 6px rgba(0,0,0,.12))}
  .card text{font-family:"Montserrat",Arial,sans-serif}
  .card--front-small{left:140px;top:352px;width:448px;height:276px}
  .card--back-small{left:608px;top:352px;width:448px;height:276px}
  .card--front-large{left:70px;top:1920px;width:520px;height:320px}
  .card--back-large{left:620px;top:1920px;width:520px;height:320px}
  .brand-lockup{position:absolute;left:60px;top:1310px;display:flex;align-items:center;gap:22px}
  .brand-lockup__dot{width:46px;height:46px;border-radius:50%;background:var(--red)}
  .brand-lockup__name{font-weight:600;font-size:62px;line-height:1.05;color:var(--charcoal);letter-spacing:2px;text-transform:uppercase}
</style>
</head>
<body>
<svg width="0" height="0" style="position:absolute">
  <defs>
    <clipPath id="card-shape"><rect width="448" height="276" rx="16"/></clipPath>

    <symbol id="card-front" viewBox="0 0 448 276">
      <g clip-path="url(#card-shape)">
        <rect width="448" height="276" fill="var(--paper)"/>
        <path d="M0,150 C120,146 200,228 448,206 L448,232 C220,254 110,180 0,182 Z" fill="var(--charcoal)"/>
        <path d="M0,196 C100,192 170,250 300,276 L0,276 Z" fill="var(--red)"/>
        <path d="M300,276 C350,262 400,250 448,246 L448,276 Z" fill="var(--red)"/>
      </g>
      <rect x=".5" y=".5" width="447" height="275" rx="16" fill="none" stroke="#dedee0"/>
      <text x="36" y="72" font-size="28" font-weight="500" fill="var(--red)">DANIEL HART</text>
      <text x="38" y="94" font-size="12" font-weight="500" fill="var(--charcoal)" letter-spacing="1">CARDIOLOGIST</text>
      <line x1="248" y1="52" x2="248" y2="160" stroke="var(--red)" stroke-width="2"/>
      <g font-size="10" fill="var(--charcoal)">
        <circle cx="266" cy="68" r="9" fill="var(--red)"/>
        <path d="M262,64 l2,-1 2,3 -1,1 q1,3 3,4 l1,-1 3,2 -1,2 q-6,0 -9,-10z" fill="#fff"/>
        <text x="282" y="72">(07) 4021 5588</text>
        <circle cx="266" cy="104" r="9" fill="var(--red)"/>
        <rect x="261" y="100" width="10" height="7" fill="none" stroke="#fff" stroke-width="1.3"/>
        <path d="M261,100 l5,4 5,-4" fill="none" stroke="#fff" stroke-width="1.3"/>
        <text x="282" y="108">info@bellmoorheart.com</text>
        <circle cx="266" cy="142" r="9" fill="var(--red)"/>
        <path d="M266,148 l-4,-6 a4,4 0 1 1 8,0z" fill="#fff"/>
        <text x="282" y="138">Suite 4, 120 Harbour Rd</text>
        <text x="282" y="151">Bellmoor QLD</text>
      </g>
      <circle cx="44" cy="240" r="6" fill="#fff"/>
      <text x="58" y="238" font-size="13" font-weight="600" fill="#fff" letter-spacing="1">BELLMOOR</text>
      <text x="58" y="254" font-size="13" font-weight="600" fill="#fff" letter-spacing="1">CARDIOLOGY</text>
    </symbol>

    <symbol id="card-back" viewBox="0 0 448 276">
      <g clip-path="url(#card-shape)">
        <rect width="448" height="276" fill="var(--paper)"/>
        <path d="M0,0 H448 V52 C330,50 230,96 120,92 C70,90 30,84 0,86 Z" fill="var(--red)"/>
        <path d="M0,86 C30,84 70,90 120,92 C230,96 330,50 448,52 L448,70 C330,70 240,116 120,112 C70,110 30,104 0,106 Z" fill="var(--grey)"/>
      </g>
      <rect x=".5" y=".5" width="447" height="275" rx="16" fill="none" stroke="#dedee0"/>
      <text x="22" y="34" font-size="11" font-weight="500" fill="#fff" letter-spacing="1">NEXT</text>
      <text x="22" y="48" font-size="11" font-weight="500" fill="#fff" letter-spacing="1">APPOINTMENTS</text>
      <circle cx="336" cy="32" r="5" fill="#fff"/>
      <text x="346" y="30" font-size="11" font-weight="600" fill="#fff" letter-spacing="1">BELLMOOR</text>
      <text x="346" y="43" font-size="11" font-weight="600" fill="#fff" letter-spacing="1">CARDIOLOGY</text>
      <g font-size="11" font-weight="500" fill="var(--charcoal)">
        <circle cx="32" cy="140" r="8" fill="var(--red)"/>
        <text x="32" y="144" font-size="10" fill="#fff" text-anchor="middle">1</text>
        <text x="120" y="138">NAME:</text>
        <line x1="160" y1="140" x2="420" y2="140" stroke="var(--line)"/>
        <text x="120" y="170">DETAILES:</text>
        <line x1="182" y1="172" x2="420" y2="172" stroke="var(--line)"/>
        <circle cx="32" cy="206" r="8" fill="var(--red)"/>
        <text x="32" y="210" font-size="10" fill="#fff" text-anchor="middle">2</text>
        <text x="120" y="204">NAME:</text>
        <line x1="160" y1="206" x2="420" y2="206" stroke="var(--line)"/>
        <text x="120" y="236">DETAILES:</text>
        <line x1="182" y1="238" x2="420" y2="238" stroke="var(--line)"/>
      </g>
    </symbol>
  </defs>
</svg>

<section class="sheet-top">
  <svg class="card card--front-small" viewBox="0 0 448 276"><use href="#card-front"/></svg>
  <svg class="card card--back-small" viewBox="0 0 448 276"><use href="#card-back"/></svg>
</section>

<section class="sheet-bottom"></section>
<div class="brand-lockup">
  <span class="brand-lockup__dot"></span>
  <span class="brand-lockup__name">Bellmoor<br>Cardiology</span>
</div>
<svg class="card card--front-large" viewBox="0 0 448 276"><use href="#card-front"/></svg>
<svg class="card card--back-large" viewBox="0 0 448 276"><use href="#card-back"/></svg>
</body>
</html>
```